Real Estate Webpage Design

We have an existing website: brindlewoodhomes.com.au
We focus customised service mainly on Property Management and second-hand property sales.
We are not entirely happy about the current design and layout can stay roughly the same as the back end coding is linked to a CRM system.
We would like to see the design are more reachable to our clients and appearing.
Please check our Website Design Draft for more details.

Industry/Entity Type

Real estate Agency

Number of Pages Required

5+ page

Font styles to use
Sans Serif

Colors

Designer to choose colors to be used in the design.

```html
<!DOCTYPE html>
<html lang="en">
<head>
<meta charset="utf-8">
<title>Brindlewood Property Group</title>
<link href="https://fonts.googleapis.com/css2?family=Inter:wght@400;500;600;700&family=Montserrat:wght@800&display=swap" rel="stylesheet">
<style>
:root{
  --navy:#1f2f5c;
  --ink:#1b1b1f;
  --muted:#8a8f99;
  --orange:#f7a446;
  --orange-light:#fbc27a;
  --pale:#f1f5f8;
  --band:#2d3e56;
  --blue:#3e6e8e;
  --form:#487c9c;
  --line:#e4e7ec;
  --white:#fff;
}
*{margin:0;padding:0;box-sizing:border-box}
html,body{width:1200px;height:4758px;overflow:hidden}
body{font-family:'Inter',sans-serif;color:var(--ink);background:var(--white);position:relative}
.abs{position:absolute}
section,header,footer{position:absolute;left:0;width:1200px}

/* hero */
.hero{top:0;height:661px}
.hero-art{left:590px;top:0;width:610px;height:545px;background:linear-gradient(135deg,#dfe6ee,#b9c7d6 60%,#eef1f5);clip-path:polygon(0 0,100% 0,100% 100%,50% 100%,20% 75%)}
.hero-house{left:600px;top:150px;width:300px;height:395px;border-radius:0 0 300px 300px;background:linear-gradient(160deg,#f3f3f3,#c9cfd6 70%,#8b7d73);}
.brand{left:85px;top:24px;display:flex;align-items:center;gap:12px}
.brand-mark{width:46px;height:46px;border:4px solid var(--orange);border-radius:4px}
.brand-name{font-size:32px;font-weight:600;color:var(--orange);line-height:1}
.brand-sub{font-size:9px;color:var(--muted);margin-top:3px}
.nav{left:495px;top:43px;display:flex;gap:17px;font-size:14px;font-weight:500;color:var(--ink)}
.nav a{color:inherit;text-decoration:none;position:relative}
.nav .active{font-weight:700}
.nav .active::after{content:"";position:absolute;left:0;right:0;bottom:-10px;height:4px;background:var(--orange)}
.hero h1{position:absolute;left:60px;top:222px;font-family:'Montserrat',sans-serif;font-weight:800;font-size:42px;line-height:49px;color:var(--navy);letter-spacing:1px}
.hero h2{position:absolute;left:60px;top:355px;font-family:'Montserrat',sans-serif;font-weight:800;font-size:40px;color:var(--navy);letter-spacing:1px}
.search{left:55px;top:433px;width:852px;height:60px;background:#fff;border-radius:30px;box-shadow:0 6px 18px rgba(0,0,0,.12);display:flex;align-items:center}
.field{padding-left:24px;height:44px;border-right:1px solid var(--line);position:relative}
.field b{display:block;font-size:14px;font-weight:600;margin-top:4px}
.field span{display:block;font-size:11px;color:var(--muted);margin-top:6px}
.field .caret{position:absolute;right:20px;top:24px;width:0;height:0;border-left:7px solid transparent;border-right:7px solid transparent;border-top:8px solid var(--orange)}
.btn-search{position:absolute;right:10px;top:10px;width:130px;height:40px;border-radius:20px;background:var(--orange-light);color:#fff;font-size:13px;font-weight:600;display:flex;align-items:center;justify-content:center;gap:6px}

/* about */
.about{top:661px;height:620px;background:var(--pale)}
.about-frame{left:105px;top:95px;width:380px;height:335px;background:#fff;clip-path:polygon(50% 0,100% 18%,100% 100%,0 100%,0 18%);box-shadow:0 0 0 1px var(--line)}
.about-photo{left:120px;top:110px;width:350px;height:305px;background:linear-gradient(180deg,#d9dde0,#c2c7cb 70%,#b79e88);clip-path:polygon(50% 0,100% 10%,100% 100%,0 100%,0 10%)}
.about-text{left:523px;top:120px;width:600px}
.about-text h3{font-size:29px;font-weight:600}
.about-text .rule{width:84px;height:5px;background:var(--orange);margin:6px 0 22px}
.about-text p{font-size:19px;line-height:24px;color:#333;margin-bottom:24px}

.achieve{top:1165px;height:296px;background:var(--band);clip-path:polygon(0 0,50% 45px,100% 0,100% 100%,0 100%)}
.achieve h3{position:absolute;top:102px;width:100%;text-align:center;color:#fff;font-size:28px;font-weight:600}
.stat{position:absolute;top:155px;text-align:center;color:#fff}
.stat b{display:block;font-size:52px;font-weight:600;color:var(--orange);line-height:1}
.stat span{display:block;font-size:19px;font-weight:600;margin-top:12px}

/* shared */
.sec-title{position:absolute;width:100%;text-align:center;font-size:29px;font-weight:700}
.sec-sub{position:absolute;width:100%;text-align:center;font-size:19px;color:#333}
.arrow{position:absolute;width:32px;height:32px;border-radius:50%;border:2px solid var(--orange);background:#fff}
.arrow::after{content:"";position:absolute;top:8px;left:9px;border-top:6px solid transparent;border-bottom:6px solid transparent}
.arrow.l::after{border-right:9px solid var(--orange)}
.arrow.r::after{left:11px;border-left:9px solid var(--orange)}
.arrow.solid{background:var(--orange);border-color:var(--orange)}
.arrow.solid.l::after{border-right-color:#fff}
.arrow.solid.r::after{border-left-color:#fff}

/* areas */
.areas{top:1500px;height:420px}
.area{position:absolute;display:flex;gap:20px;align-items:center}
.area .pic{width:100px;height:100px;border-radius:8px}
.area b{display:block;font-size:16px;font-weight:600}
.area span{display:block;font-size:16px;color:var(--muted);margin-top:12px}

/* properties */
.props{top:2020px;height:520px}
.tabs{position:absolute;top:133px;left:0;width:100%;text-align:center;font-size:16px}
.tabs span{margin:0 28px;position:relative}
.tabs .on::after{content:"";position:absolute;left:-4px;right:-4px;bottom:-10px;height:3px;background:var(--orange)}
.card{position:absolute;top:177px;width:248px}
.card .pic{height:151px;position:relative}
.card .heart{position:absolute;right:8px;top:8px;width:26px;height:26px;border-radius:5px;background:#fff;opacity:.85}
.card h4{font-size:16px;font-weight:600;margin:12px 0 0 10px}
.card .addr{font-size:13px;margin:6px 0 0 10px}
.card .feat{font-size:12px;color:var(--muted);margin:12px 0 0 10px;padding-bottom:12px;border-bottom:1px solid var(--line)}
.card .price{font-size:14px;font-weight:600;margin:18px 0 0 10px}
.card .agent{position:absolute;right:12px;bottom:-4px;width:32px;height:32px;border-radius:50%;background:#6f7a84}

/* explore */
.explore{top:2630px;height:578px;background:var(--blue)}
.explore .sec-title{color:#fff;top:70px}
.explore .sec-sub{color:#fff;top:113px}
.tile{position:absolute;top:180px;width:194px;height:282px;display:flex;align-items:flex-end;justify-content:center;padding-bottom:80px;color:#fff;font-size:17px;font-weight:600}

/* blog */
.blog{top:3290px;height:430px}
.feature{left:83px;top:120px;width:334px;height:273px;background:linear-gradient(120deg,#f2f2f0,#dcdcd8);padding:40px 26px}
.feature small{font-size:11px}
.feature h4{font-size:19px;font-weight:700;line-height:23px;margin:10px 0 12px}
.feature p{font-size:11px;line-height:13px}
.btn{display:inline-block;background:var(--orange);color:#fff;font-size:11px;font-weight:600;padding:7px 16px;border-radius:3px;margin-top:18px}
.post{position:absolute;width:340px;height:122px;display:flex;gap:10px}
.post .pic{width:125px;height:122px;flex:none}
.post small{font-size:10px;color:#444}
.post h5{font-size:13px;font-weight:700;line-height:15px;margin:5px 0}
.post p{font-size:10px;line-height:12px;color:#444}
.post a{display:block;font-size:11px;color:var(--orange);margin-top:6px;text-decoration:underline}

/* contact */
.contact{top:3849px;height:428px;background:var(--pale)}
.contact-photo{left:772px;top:0;width:428px;height:428px;background:linear-gradient(180deg,#d8c6b4,#efe8df 45%,#c7802e 70%,#7c6d61)}
.contact h3{position:absolute;left:83px;top:120px;font-size:31px;font-weight:700;line-height:37px}
.contact p{position:absolute;left:83px;top:205px;width:440px;font-size:19px;line-height:24px;color:#333}
.form{left:587px;top:55px;width:312px;height:318px;background:var(--form);padding:28px 25px}
.input{background:#fff;height:38px;border-radius:3px;font-size:11px;color:var(--muted);padding:12px 14px;margin-bottom:15px}
.input.tall{height:80px}
.form .btn{margin-top:2px;padding:8px 14px;font-size:10px}

/* footer */
.footer{top:4366px;height:392px;background:linear-gradient(160deg,#b7c7d6,#dde5ec 45%,#aebfcf)}
.foot-panel{left:44px;top:46px;width:1110px;height:328px;background:rgba(243,246,249,.93)}
.fcol{position:absolute;top:100px;font-size:12px;color:#333}
.fcol h6{font-size:16px;font-weight:500;margin-bottom:16px;color:var(--ink)}
.fcol li{list-style:none;margin-bottom:11px}
.contact-row{display:flex;gap:10px;align-items:flex-start;font-size:11px;color:var(--muted);margin-bottom:16px;line-height:14px}
.social{display:flex;gap:16px;margin-top:16px}
.social i{width:12px;height:12px;background:var(--ink);border-radius:2px;display:block}
.sub-input{width:200px;height:36px;background:#fff;font-size:11px;color:var(--muted);padding:11px 14px;display:inline-block}
.sub-btn{display:inline-block;vertical-align:top;margin-left:12px;width:44px;height:38px;background:var(--orange-light);border-radius:3px}
</style>
</head>
<body>

<header class="hero">
  <div class="abs hero-art" role="img" aria-label="Pale geometric glass facade backdrop"></div>
  <div class="abs hero-house" role="img" aria-label="Hand holding a model two-storey house"></div>
  <div class="abs brand">
    <div class="brand-mark"></div>
    <div><div class="brand-name">Brindlewood</div><div class="brand-sub">Property Group</div></div>
  </div>
  <nav class="abs nav">
    <a class="active">HOME</a><a>ABOUT US</a><a>LEASING</a><a>BUY</a><a>SELL</a><a>OUR TEAM</a><a>BLOG</a><a>CONTACT US</a>
  </nav>
  <h1>PLAN YOUR FUTURE<br>PROPERTY WITH US</h1>
  <h2>ARE YOU READY ?</h2>
  <div class="abs search">
    <div class="field" style="width:208px"><b>TYPE</b><span>Property Type</span><i class="caret"></i></div>
    <div class="field" style="width:170px"><b>LOCATION</b><span>All Cities</span><i class="caret"></i></div>
    <div class="field" style="border:none"><b>SEARCH</b><span>Enter Keywords</span></div>
    <div class="btn-search">
      <svg width="14" height="14" viewBox="0 0 14 14" fill="none" stroke="#fff" stroke-width="2"><circle cx="6" cy="6" r="4.5"/><path d="M9.5 9.5L13 13"/></svg>SEARCH
    </div>
  </div>
</header>

<section class="about">
  <div class="abs about-frame"></div>
  <div class="abs about-photo" role="img" aria-label="Two hands passing a small model house"></div>
  <div class="abs about-text">
    <h3>Brindlewood</h3>
    <div class="rule"></div>
    <p>Brindlewood means a home built to last. Buying a property is one of the most expensive and important assets for people. Brindlewood is a real estate company located in Gungahlin, Canberra.</p>
    <p>Being a portfolio sales agent and property manager, coupled with our high–profile international real estate experience, Brindlewood is considered a market leader on the cutting edge with deep industry knowledge, ranging from landlord–tenant relationships, residential purchases.</p>
  </div>
</section>

<section class="achieve">
  <h3>Our Achievments</h3>
  <div class="stat" style="left:355px;width:160px"><b>2,763</b><span>Propreties Sold</span></div>
  <div class="stat" style="left:650px;width:200px"><b>1,682</b><span>Propreties Leased</span></div>
</section>

<section class="areas">
  <h3 class="sec-title" style="top:43px">Areas We Serve</h3>
  <p class="sec-sub" style="top:86px">Explore our areas to find your future property</p>
  <div class="arrow l" style="left:42px;top:244px"></div>
  <div class="arrow r" style="left:1125px;top:244px"></div>
  <div class="area" style="left:103px;top:145px"><div class="pic" role="img" aria-label="Canberra at night" style="background:linear-gradient(#1c2140,#b06a3a)"></div><div><b>Canberra</b><span>24 Listings</span></div></div>
  <div class="area" style="left:365px;top:145px"><div class="pic" role="img" aria-label="Newcastle bridge" style="background:linear-gradient(#8fb4d8,#6a6f77)"></div><div><b>Newcastle</b><span>24 Listings</span></div></div>
  <div class="area" style="left:628px;top:145px"><div class="pic" role="img" aria-label="Los Angeles palms at sunset" style="background:linear-gradient(#d6693a,#3a2a2a)"></div><div><b>Los Angeles</b><span>24 Listings</span></div></div>
  <div class="area" style="left:890px;top:145px"><div class="pic" role="img" aria-label="Paris tower" style="background:linear-gradient(#8ec3e8,#d9e6ef)"></div><div><b>Paris</b><span>24 Listings</span></div></div>
  <div class="area" style="left:103px;top:278px"><div class="pic" role="img" aria-label="Melbourne streets" style="background:linear-gradient(#9fb9cf,#6c6a5f)"></div><div><b>Melbourne</b><span>24 Listings</span></div></div>
  <div class="area" style="left:365px;top:278px"><div class="pic" role="img" aria-label="London street with red bus" style="background:linear-gradient(#c9c4c0,#a0413f)"></div><div><b>London</b><span>24 Listings</span></div></div>
  <div class="area" style="left:628px;top:278px"><div class="pic" role="img" aria-label="Auckland skyline over water" style="background:linear-gradient(#b6cbd6,#4f7184)"></div><div><b>Auckland</b><span>24 Listings</span></div></div>
  <div class="area" style="left:890px;top:278px"><div class="pic" role="img" aria-label="Miami towers and palms" style="background:linear-gradient(#f2f2f2,#6e8da0)"></div><div><b>Miami</b><span>24 Listings</span></div></div>
</section>

<section class="props">
  <h3 class="sec-title" style="top:22px">Our Lates Properties</h3>
  <p class="sec-sub" style="top:68px">Lorem ipsum dolor sit amet, consectetur adipiscing elit.</p>
  <div class="tabs"><span>FOR SALE</span><span class="on">FOR LEASE</span></div>
  <div class="arrow l" style="left:42px;top:348px"></div>
  <div class="arrow r" style="left:1125px;top:348px"></div>
  <div class="card" style="left:81px"><div class="pic" role="img" aria-label="Bright living room" style="background:linear-gradient(#e9e4dc,#bfa98a)"><i class="heart"></i></div><h4>Canberra</h4><div class="addr">14 Larkspur Street Red Hill</div><div class="feat">▭ 2 &nbsp; ▭ 2 &nbsp; ▭ 2 &nbsp; ☐ 800 Sqm</div><div style="position:relative"><div class="price">$379,8/mo</div><i class="agent"></i></div></div>
  <div class="card" style="left:345px"><div class="pic" role="img" aria-label="Grey lounge with fireplace" style="background:linear-gradient(#cfcfcf,#7d7b78)"><i class="heart"></i></div><h4>Melbourne</h4><div class="addr">3/27 Finch Lane</div><div class="feat">▭ 2 &nbsp; ▭ 2 &nbsp; ▭ 2 &nbsp; ☐ 910 Sqm</div><div style="position:relative"><div class="price">$431,3/mo</div><i class="agent"></i></div></div>
  <div class="card" style="left:609px"><div class="pic" role="img" aria-label="White modern house" style="background:linear-gradient(#f4f4f4,#c9ced2)"><i class="heart"></i></div><h4>Miami</h4><div class="addr">NW 41st Terrace</div><div class="feat">▭ 3 &nbsp; ▭ 5 &nbsp; ▭ 2 &nbsp; ☐ 2100 Sqm</div><div style="position:relative"><div class="price">$1429,8/mo</div><i class="agent"></i></div></div>
  <div class="card" style="left:871px"><div class="pic" role="img" aria-label="Large family house with lawn" style="background:linear-gradient(#8fb3d4,#5f7a4a)"><i class="heart"></i></div><h4>Auckland</h4><div class="addr">56 Kowhai Crescent</div><div class="feat">▭ 3 &nbsp; ▭ 2 &nbsp; ▭ 2 &nbsp; ☐ 1800 Sqm</div><div style="position:relative"><div class="price">$1352,7/mo</div><i class="agent"></i></div></div>
</section>

<section class="explore">
  <h3 class="sec-title">Explore Our Properties</h3>
  <p class="sec-sub">Lorem ipsum dolor sit amet, consectetur adipiscing elit.</p>
  <div class="arrow solid l" style="left:42px;top:304px"></div>
  <div class="arrow solid r" style="left:1125px;top:304px"></div>
  <div class="tile" style="left:83px;background:linear-gradient(#7f97ad,#3c4a3e)" role="img" aria-label="House exterior">House</div>
  <div class="tile" style="left:293px;background:linear-gradient(#8a8f92,#a4532c)" role="img" aria-label="Room with sofa">Room</div>
  <div class="tile" style="left:504px;background:linear-gradient(#6f6a63,#3f4b56)" role="img" aria-label="Villa with pool">Villa</div>
  <div class="tile" style="left:714px;background:linear-gradient(#4c5156,#2a2d30)" role="img" aria-label="Apartment towers">Apartment</div>
  <div class="tile" style="left:923px;background:linear-gradient(#6a6d6e,#4a3a33)" role="img" aria-label="Office interior">Office</div>
</section>

<section class="blog">
  <h3 class="sec-title" style="top:24px">From Our Blog</h3>
  <p class="sec-sub" style="top:68px">Lorem ipsum dolor sit amet, consectetur adipiscing elit.</p>
  <div class="abs feature" role="img" aria-label="Laptop on a desk behind article text">
    <small>Tom Reyes . 24 May . 3 min read</small>
    <h4>How Long Does It Take<br>to Find a Tenant ?</h4>
    <p>Lorem ipsum dolor sit amet, consectetur adipiscing elit. Morbi eget ultricies sed amet amet elementum faucibus lorem. Enim et massa volutpat at nulla tincidunt suspendisse integer massa.</p>
    <span class="btn">Read More</span>
  </div>
  <div class="post" style="left:432px;top:120px"><div class="pic" role="img" aria-label="Keys beside a model house" style="background:linear-gradient(#dfe3e6,#a33a2f)"></div><div><small>Liam Hart . 08 May . 3 min read</small><h5>For Protect Your Property</h5><p>Lorem ipsum dolor sit amet, consect adipiscing elit. Augue vel lectus mol massa id lectus.</p><a>Read More</a></div></div>
  <div class="post" style="left:785px;top:120px"><div class="pic" role="img" aria-label="Person working at a laptop" style="background:linear-gradient(#c9d0d6,#3c4a5a)"></div><div><small>Nina Vale . 05 May . 3 min read</small><h5>What You Should Know Before Start Renting ?</h5><p>Lorem ipsum dolor sit amet, consect adipiscing elit. Augue vel lectus mol massa id lectus.</p><a>Read More</a></div></div>
  <div class="post" style="left:432px;top:269px"><div class="pic" role="img" aria-label="Team meeting in an office" style="background:linear-gradient(#cdd6dd,#e07a2f)"></div><div><small>Ella Brook . 17 May . 3 min read</small><h5>Increase Your Housing Project Sales 3x Faster!</h5><p>Lorem ipsum dolor sit amet, consect adipiscing elit. Augue vel lectus mol massa id lectus.</p><a>Read More</a></div></div>
  <div class="post" style="left:785px;top:269px"><div class="pic" role="img" aria-label="Renovated hallway" style="background:linear-gradient(#2b3440,#a68d5e)"></div><div><small>Nina Vale . 05 May . 3 min read</small><h5>Renovating an Existing Home instead of Buying a New House</h5><p>Lorem ipsum dolor sit amet, consect adipiscing elit. Augue vel lectus mol massa id lectus.</p><a>Read More</a></div></div>
</section>

<section class="contact">
  <div class="abs contact-photo" role="img" aria-label="Living room with orange armchair"></div>
  <h3>We Help You Buy or Sell<br>Your Property</h3>
  <p>Lorem ipsum dolor sit amet, consectetur adipiscing elit. Commodo mattis feugiat morbi gravida. Consequat aliquet sitvitae quam lacus nulla cras vulputate. Leo quis egestas ultrices morbi nunc, eu.</p>
  <div class="abs form">
    <div class="input">Your Name</div>
    <div class="input">E-mail/Phone</div>
    <div class="input tall">Message</div>
    <span class="btn">Send Message</span>
  </div>
</section>

<footer class="footer">
  <div class="abs foot-panel"></div>
  <div class="fcol" style="left:78px;width:200px">
    <h6>About</h6>
    <div class="contact-row"><svg width="12" height="14" viewBox="0 0 12 14" fill="none" stroke="#666"><path d="M6 13S1 8 1 5a5 5 0 0110 0c0 3-5 8-5 8z"/><circle cx="6" cy="5" r="1.8"/></svg><span>18 Harlow Lane,<br>Gungahlin, ACT, 2912</span></div>
    <div class="contact-row"><svg width="12" height="12" viewBox="0 0 12 12" fill="none" stroke="#666"><path d="M2 1h2l1 3-1.5 1a7 7 0 003.5 3.5L8 7l3 1v2a1 1 0 01-1 1A9 9 0 011 2a1 1 0 011-1z"/></svg><span>02 6000 1234</span></div>
    <div class="contact-row"><svg width="13" height="10" viewBox="0 0 13 10" fill="none" stroke="#666"><rect x=".5" y=".5" width="12" height="9"/><path d="M.5.5l6 5 6-5"/></svg><span>hello@brindlewoodhomes.com.au</span></div>
    <div class="social"><i></i><i></i><i></i><i></i></div>
  </div>
  <div class="fcol" style="left:420px"><h6>Discover</h6><ul><li>Canberra</li><li>Melbourne</li><li>Perth</li><li>Newcastle</li></ul></div>
  <div class="fcol" style="left:540px"><h6>Lists by Category</h6><ul><li>House</li><li>Room</li><li>Apartment</li><li>Villa</li><li>Office</li></ul></div>
  <div class="fcol" style="left:718px"><h6>Quick Access</h6><ul><li>About Us</li><li>Leasing</li><li>Buy</li><li>Sell</li><li>Our Team</li><li>Blog</li></ul></div>
  <div class="fcol" style="left:860px"><h6>Subscribe</h6><span class="sub-input">Your E-mail</span><span class="sub-btn"></span></div>
</footer>

</body>
</html>
```